Building Servicess

We need a new business card design for a company. We specialise in: Electrical/Site temporary electrics, Data/Network Installation, Passive Fire Protection

Industry/Entity Type

Construction

Contact Information for Business Card

Services provided as detailed on project description

Font styles to use
Serif

Colors
0054AA
0677BA
7BADD7
CADEEF
E8F1F8
00AB8E
00BBA5
67D7C9
C6EFE9
E9F9F6
EB3D1F
EC4F4E
F09395
F8D3D4
FCEDEE

Requirements
Must have
• Company logo-contact details-phone numbers

```html
<!DOCTYPE html>
<html lang="en">
<head>
<meta charset="utf-8">
<title>Norvale Solution Services – Business Card</title>
<link href="https://fonts.googleapis.com/css2?family=Montserrat:wght@500;600;700&family=Open+Sans:wght@400;600&display=swap" rel="stylesheet">
<style>
  :root{
    --blue-deep:#0054AA;
    --blue:#0677BA;
    --blue-bright:#1E9BE0;
    --blue-light:#7BADD7;
    --grey:#8A8D91;
    --grey-band:#9A9DA1;
    --ink:#4A4D52;
    --paper:#FFFFFF;
    --paper-shade:#EEF0F2;
    --bg:#2B2D30;
  }
  *{margin:0;padding:0;box-sizing:border-box}
  html,body{width:1200px;height:874px;overflow:hidden}
  body{background:var(--bg);position:relative;font-family:"Open Sans",Arial,sans-serif}

  .card{position:absolute;left:280px;width:640px;height:366px;overflow:hidden;box-shadow:0 12px 30px rgba(0,0,0,.45)}

  /* back side */
  .card--back{top:50px}
  .card--back .pattern-field{position:absolute;inset:0;
    background:linear-gradient(115deg,#2BB4EC 0%,var(--blue-bright) 30%,var(--blue) 60%,var(--blue-deep) 100%)}
  .card--back .back-brand{position:absolute;right:40px;bottom:34px;display:flex;align-items:center;gap:8px;
    font-family:"Montserrat",Arial,sans-serif;font-weight:700;font-size:20px;color:var(--paper);letter-spacing:1px}
  .back-brand .brand-square{width:14px;height:14px;background:var(--paper)}

  /* front side */
  .card--front{top:458px;background:linear-gradient(120deg,var(--paper) 55%,var(--paper-shade) 100%)}
  .brand{position:absolute;left:46px;top:70px;width:250px;font-family:"Montserrat",Arial,sans-serif}
  .brand-name{display:block;font-weight:700;font-size:40px;color:var(--blue);letter-spacing:1px;line-height:1}
  .brand-sub{display:block;font-weight:600;font-size:19px;color:var(--blue);letter-spacing:.5px;margin-top:10px;
    padding-top:6px;border-top:2px solid var(--grey)}
  .brand-ltd{display:block;text-align:right;font-size:9px;letter-spacing:5px;color:var(--grey);margin-top:2px}

  .divider{position:absolute;left:325px;top:62px;width:1px;height:150px;background:#C9CCD0}

  .contact{position:absolute;left:345px;top:66px;font-size:14px;color:var(--ink)}
  .contact-name{font-family:"Montserrat",Arial,sans-serif;font-weight:700;font-size:21px;color:var(--blue);letter-spacing:.5px}
  .contact-role{color:var(--grey);font-size:14px;margin:0 0 12px}
  .contact-list{list-style:none}
  .contact-list li{display:flex;align-items:center;gap:10px;line-height:21px}
  .contact-list svg{width:12px;height:12px;fill:var(--blue)}

  .services-band{position:absolute;left:0;top:242px;width:440px;height:74px;background:var(--blue);
    color:var(--paper);font-size:15px;line-height:22px;padding:10px 0 0 70px}
  .band-mark{position:absolute;left:452px;top:268px;width:40px;height:40px;background:var(--blue)}
  .grey-band{position:absolute;left:502px;top:290px;width:138px;height:40px;background:var(--grey-band)}
</style>
</head>
<body>

<section class="card card--back" aria-label="Card back">
  <div class="pattern-field" role="img" aria-label="Repeating company mark pattern in blue tones"></div>
  <div class="back-brand"><span class="brand-square"></span>NORVALE</div>
</section>

<section class="card card--front" aria-label="Card front">
  <div class="brand">
    <span class="brand-name">NORVALE</span>
    <span class="brand-sub">SOLUTION SERVICES</span>
    <span class="brand-ltd">LTD</span>
  </div>

  <div class="divider"></div>

  <div class="contact">
    <div class="contact-name">DANIEL HARTLEY</div>
    <div class="contact-role">President</div>
    <ul class="contact-list">
      <li><svg viewBox="0 0 24 24"><path d="M6.6 10.8a15 15 0 0 0 6.6 6.6l2.2-2.2c.3-.3.7-.4 1-.2 1.1.4 2.3.6 3.6.6.6 0 1 .4 1 1V20c0 .6-.4 1-1 1A17 17 0 0 1 3 4c0-.6.4-1 1-1h3.5c.6 0 1 .4 1 1 0 1.3.2 2.5.6 3.6.1.3 0 .7-.2 1z"/></svg>555-214-0193</li>
      <li><svg viewBox="0 0 24 24"><path d="M7 1h10a2 2 0 0 1 2 2v18a2 2 0 0 1-2 2H7a2 2 0 0 1-2-2V3a2 2 0 0 1 2-2zm0 3v14h10V4z"/></svg>555-618-2740</li>
      <li><svg viewBox="0 0 24 24"><path d="M2 4h20v16H2zm2 2v.5l8 5 8-5V6z"/></svg>info@norvalesolutions.com</li>
      <li><svg viewBox="0 0 24 24"><circle cx="12" cy="12" r="10"/></svg>www.norvalesolutions.com</li>
    </ul>
  </div>

  <div class="services-band">
    Electrical/Site temporary electrics Data/<br>
    Network Installation • Passive Fire Protection
  </div>
  <div class="band-mark"></div>
  <div class="grey-band"></div>
</section>

</body>
</html>
```